Environmental Group Website Template

We want a website template for an environmental cause. The website should have a dark content area that is transparent. The website text and icons are white.
The background is a nature scene. The background image repeats.
Industry/Entity Type
Group

```html
<!DOCTYPE html>
<html lang="en">
<head>
<meta charset="utf-8">
<title>Verdant Collective</title>
<link href="https://fonts.googleapis.com/css2?family=Lato:wght@400;700&family=Questrial&display=swap" rel="stylesheet">
<style>
:root{
  --white:#ffffff;
  --ink:#1b1b1b;
  --muted:#6a6a6a;
  --panel:rgba(22,32,48,0.55);
  --search-bg:#c9d9ea;
  --blue-top:#1a8fe0;
  --blue-bottom:#0a4fa8;
  --band:#f5f5f5;
  --green-top:#4fae3f;
  --green-bottom:#1f7a2e;
  --dot-active:#3a9a3a;
}
*{margin:0;padding:0;box-sizing:border-box}
html,body{width:1200px;height:958px;overflow:hidden;background:var(--white)}
body{position:relative;font-family:"Lato",sans-serif;color:var(--white)}
.hero{position:absolute;left:0;top:0;width:1200px;height:569px;overflow:hidden}
.hero-scene{position:absolute;inset:0;
  background:
    linear-gradient(90deg, rgba(0,0,0,0) 0%, rgba(0,0,0,0) 55%, rgba(4,20,50,0.55) 75%, rgba(4,20,50,0.65) 100%),
    linear-gradient(180deg,#1d4f8f 0%,#3d6ea3 12%,#e49a74 22%,#f2b07a 26%,#1f2b3c 34%,#c78a74 42%,#5e86b5 58%,#4c8fc9 80%,#2a78bf 100%);}
.hero-panel{position:absolute;left:413px;top:0;width:360px;height:569px;background:var(--panel);
  box-shadow:-6px 0 10px rgba(0,0,0,0.25),6px 0 10px rgba(0,0,0,0.25)}
.phone{position:absolute;left:131px;top:12px;display:flex;align-items:center;gap:8px;font-weight:700;font-size:16px}
.nav{position:absolute;top:54px;display:flex;list-style:none;font-weight:700;font-size:15px}
.nav li{padding:0 17px;border-left:1px solid rgba(255,255,255,0.8);line-height:17px}
.nav li:first-child{border-left:none}
.nav-left{left:119px}
.nav-right{left:790px}
.nav-right li{padding:0 29px}
.brand{position:absolute;left:498px;top:30px;display:flex;align-items:center;gap:12px}
.brand-dot{width:40px;height:40px;border-radius:50%;background:var(--green-top)}
.brand-name{font-family:"Questrial",sans-serif;font-size:28px;line-height:30px;color:var(--white)}
.search{position:absolute;left:870px;top:7px;width:199px;height:27px;background:var(--search-bg);
  display:flex;align-items:center;justify-content:space-between;padding:0 8px 0 9px;font-size:14px;color:#333}
.hero-text{position:absolute;left:413px;top:231px;width:360px;text-align:center;font-family:"Questrial",sans-serif;font-size:18px;line-height:27px;padding:0 40px}
.dots{position:absolute;left:571px;top:537px;display:flex;gap:9px}
.dots span{width:14px;height:14px;border-radius:50%;background:var(--white)}
.dots span.active{border:3px solid var(--white);background:var(--dot-active)}
.features{position:absolute;left:0;top:569px;width:1200px;height:338px}
.feature-band{position:absolute;left:427px;top:0;width:346px;height:338px;background:var(--band)}
.feature{position:absolute;top:0;width:346px;text-align:center}
.feature-icon{width:116px;height:116px;margin:45px auto 0;border-radius:50%;border:3px solid #eef3f8;
  background:linear-gradient(180deg,var(--blue-top),var(--blue-bottom));box-shadow:0 1px 3px rgba(0,0,0,0.15)}
.feature-shadow{width:96px;height:8px;margin:20px auto 0;border-radius:50%;background:radial-gradient(ellipse,rgba(0,0,0,0.14),rgba(0,0,0,0))}
.feature-title{margin-top:12px;font-family:"Questrial",sans-serif;font-size:22px;color:var(--ink);font-weight:400}
.feature-text{margin-top:10px;font-size:17px;line-height:25px;color:var(--muted)}
.footer{position:absolute;left:0;top:907px;width:1200px;height:51px;background:linear-gradient(180deg,var(--green-top),var(--green-bottom))}
.social{position:absolute;left:132px;top:16px;display:flex;gap:17px}
.social span{width:18px;height:18px;border-radius:50%;background:rgba(255,255,255,0.85)}
.copyright{position:absolute;right:131px;top:16px;font-family:"Questrial",sans-serif;font-size:15px}
</style>
</head>
<body>
<header class="hero">
  <div class="hero-scene" role="img" aria-label="Photo of a calm lake at sunset with reeds silhouetted on the right"></div>
  <div class="hero-panel"></div>
  <div class="phone">
    <svg width="18" height="18" viewBox="0 0 24 24" aria-hidden="true"><path fill="#fff" d="M6.6 10.8c1.4 2.8 3.8 5.1 6.6 6.6l2.2-2.2c.3-.3.7-.4 1-.2 1.1.4 2.3.6 3.6.6.6 0 1 .4 1 1V20c0 .6-.4 1-1 1C10.6 21 3 13.4 3 4c0-.6.4-1 1-1h3.5c.6 0 1 .4 1 1 0 1.3.2 2.5.6 3.6.1.3 0 .7-.2 1z"/></svg>
    123 456 7890
  </div>
  <ul class="nav nav-left"><li>About Us</li><li>Explore</li><li>Challenges</li></ul>
  <div class="brand"><span class="brand-dot"></span><span class="brand-name">Verdant<br>Collective</span></div>
  <div class="search">Search
    <svg width="15" height="15" viewBox="0 0 16 16" aria-hidden="true"><circle cx="6.5" cy="6.5" r="4.5" fill="none" stroke="#333" stroke-width="2"/><path d="M10 10l4.5 4.5" stroke="#333" stroke-width="2.4" stroke-linecap="round"/></svg>
  </div>
  <ul class="nav nav-right"><li>Solutions</li><li>Events</li><li>News</li></ul>
  <p class="hero-text">Lorem Ipsum Dolor Sit Amet, Consectetuer Adipiscing Elit V Sed Diam Nonummy Nibh Euismod Tincidunt Ut sit alm Laoreet Dolore Magna sit Aliquam Erat Volutpa Ut Wisi Lorem Ipsum Dolor Sit Amet</p>
  <div class="dots"><span class="active"></span><span></span><span></span></div>
</header>

<section class="features">
  <div class="feature-band"></div>
  <article class="feature" style="left:88px">
    <div class="feature-icon" role="img" aria-label="Volunteer icon"></div>
    <div class="feature-shadow"></div>
    <h2 class="feature-title">Volunteer with Us</h2>
    <p class="feature-text">Lorem ipsum dolor sit amet,<br>consectetur adipiscing eliterw</p>
  </article>
  <article class="feature" style="left:427px">
    <div class="feature-icon" role="img" aria-label="Donate icon"></div>
    <div class="feature-shadow"></div>
    <h2 class="feature-title">Support Our Work</h2>
    <p class="feature-text">Lorem ipsum dolor sit amet,<br>consectetur adipiscing eliterw</p>
  </article>
  <article class="feature" style="left:767px">
    <div class="feature-icon" role="img" aria-label="Campaign group icon"></div>
    <div class="feature-shadow"></div>
    <h2 class="feature-title">Make Your Voice Heard</h2>
    <p class="feature-text">Lorem ipsum dolor sit amet,<br>consectetur adipiscing eliterw</p>
  </article>
</section>

<footer class="footer">
  <div class="social"><span></span><span></span><span></span><span></span><span></span><span></span></div>
  <p class="copyright">© 2015 VerdantCollective. All Rights Reserved.</p>
</footer>
</body>
</html>
```